Business Card Design

I need a business card for a new company based in Australia called "MedLinkora".

Its a cloud program for GPs that allows them to search for the specialist they require using a simple user friendly tool.

I would like the colours to match those in the program (the colours in the logo attached).

The final design should reflect the programs clarity, ease of use and professionalism.

Target Market(s)

GPs and other Health Professionals

Industry/Entity Type

Business

Contact Information for Business Card

MedLinkora; The Trusted Clinician Index; Marla Ostrove CEO; 0438215906; marla@medlinkora.example; www.medlinkora.example

Requirements
Must have
• Must have the logo attached; the web address and my name and phone number
Nice to have
• the slogan "The Trusted Clinician Index"

```html
<!DOCTYPE html>
<html lang="en">
<head>
<meta charset="utf-8">
<title>MedLinkora Business Card</title>
<link rel="stylesheet" href="https://fonts.googleapis.com/css2?family=Questrial&family=Open+Sans:wght@400;700&display=swap">
<style>
  :root {
    --brand-cyan: #1fa9dd;
    --brand-grey: #a3a5a8;
    --text-grey: #8a8c8f;
    --card-white: #ffffff;
    --card-black: #050505;
    --stage: #e9e9e7;
    --on-dark: #e6e6e6;
  }
  * { box-sizing: border-box; margin: 0; padding: 0; }
  html, body { width: 1200px; height: 829px; overflow: hidden; }
  body { background: var(--stage); position: relative; font-family: "Open Sans", Arial, sans-serif; }

  .card {
    position: absolute;
    width: 540px;
    height: 309px;
    overflow: hidden;
    box-shadow: 0 6px 18px rgba(0,0,0,0.18);
  }
  .card--front { left: 40px; top: 190px; background: var(--card-white); }
  .card--back  { left: 620px; top: 330px; background: var(--card-black); }

  .card__swoosh { position: absolute; inset: 0; width: 100%; height: 100%; }

  .brand__name {
    font-family: "Questrial", Arial, sans-serif;
    color: var(--brand-cyan);
    font-weight: 400;
    letter-spacing: -0.5px;
    line-height: 1;
  }
  .brand__tagline {
    font-family: "Questrial", Arial, sans-serif;
    color: var(--text-grey);
    line-height: 1;
  }

  .card--front .brand { position: absolute; left: 34px; top: 60px; }
  .card--front .brand__name { font-size: 44px; }
  .card--front .brand__tagline { font-size: 13px; margin-top: 4px; margin-left: 2px; }

  .person { position: absolute; left: 36px; top: 180px; }
  .person__name { color: var(--brand-cyan); font-weight: 700; font-size: 17px; }
  .person__role { color: var(--text-grey); font-size: 13px; margin-top: 2px; }

  .contact {
    position: absolute;
    right: 18px;
    top: 38px;
    list-style: none;
    color: var(--card-white);
    font-size: 11.5px;
    text-align: right;
  }
  .contact__item { display: flex; align-items: center; justify-content: flex-end; gap: 6px; height: 24px; }
  .contact__icon { width: 13px; height: 13px; flex: none; }

  .card--back .brand {
    position: absolute; left: 0; right: 0; top: 92px; text-align: center;
  }
  .card--back .brand__name { font-size: 58px; }
  .card--back .brand__tagline { font-size: 15px; margin-top: 6px; }
  .card--back .web {
    position: absolute; left: 0; right: 0; top: 215px; text-align: center;
    color: var(--on-dark); font-size: 15px; letter-spacing: 1.5px;
  }
</style>
</head>
<body>
  <section class="card card--front">
    <svg class="card__swoosh" viewBox="0 0 540 309" aria-hidden="true">
      <path d="M300 0 C270 150 170 245 0 290 L0 300 C185 255 285 155 318 0 Z" fill="var(--brand-grey)"/>
      <path d="M0 272 C150 250 240 200 270 150 C230 215 140 262 0 282 Z" fill="var(--brand-grey)" opacity="0.55"/>
      <path d="M340 0 C310 150 220 255 60 309 L540 309 L540 0 Z" fill="var(--brand-cyan)"/>
      <path d="M330 0 C300 150 210 255 50 309 L60 309 C220 255 310 150 340 0 Z" fill="var(--card-white)"/>
    </svg>

    <div class="brand">
      <div class="brand__name">MedLinkora</div>
      <div class="brand__tagline">The Trusted Clinician Index</div>
    </div>

    <div class="person">
      <div class="person__name">Marla Ostrove</div>
      <div class="person__role">CEO</div>
    </div>

    <ul class="contact">
      <li class="contact__item">
        <svg class="contact__icon" viewBox="0 0 16 16" aria-hidden="true"><circle cx="8" cy="8" r="7.5" fill="none" stroke="#fff" stroke-width="1.2"/><path d="M5.5 4.5 l1.5 0 l0.6 2 l-1 0.8 a5 5 0 0 0 2.2 2.2 l0.8 -1 l2 0.6 l0 1.5 a1 1 0 0 1 -1 1 A6 6 0 0 1 4.5 5.5 a1 1 0 0 1 1 -1Z" fill="#fff"/></svg>
        <span>0438215906</span>
      </li>
      <li class="contact__item">
        <svg class="contact__icon" viewBox="0 0 16 16" aria-hidden="true"><circle cx="8" cy="8" r="8" fill="#fff"/><rect x="3.5" y="5" width="9" height="6" fill="var(--brand-cyan)"/><path d="M3.5 5 L8 8.5 L12.5 5" fill="none" stroke="#fff" stroke-width="1"/></svg>
        <span>marla@medlinkora.example</span>
      </li>
      <li class="contact__item">
        <svg class="contact__icon" viewBox="0 0 16 16" aria-hidden="true"><circle cx="8" cy="8" r="7" fill="none" stroke="#fff" stroke-width="1.4"/><ellipse cx="8" cy="8" rx="3" ry="7" fill="none" stroke="#fff" stroke-width="1.1"/><path d="M1 8 H15 M2.5 4.5 H13.5 M2.5 11.5 H13.5" stroke="#fff" stroke-width="1"/></svg>
        <span>www.medlinkora.example</span>
      </li>
    </ul>
  </section>

  <section class="card card--back">
    <div class="brand">
      <div class="brand__name">MedLinkora</div>
      <div class="brand__tagline">The Trusted Clinician Index</div>
    </div>
    <div class="web">www.medlinkora.example</div>
  </section>
</body>
</html>
```